Wordpress Theme, Folder, Brochure

Hello,

I have 3 projects that need to be completed and they all need to be the same theme.

Wordpress Theme:
Design homepage and one internal page

Print Folder:
I need a folder designed to match the website

Trifold Brochure:
I need a generic tri-fold brochure build to match the theme

Please find the attached file for more info.

Rolf

```html
<!DOCTYPE html>
<html lang="en">
<head>
<meta charset="utf-8">
<title>Harborline PEO</title>
<link href="https://fonts.googleapis.com/css2?family=PT+Sans:wght@400;700&display=swap" rel="stylesheet">
<style>
:root{
  --blue:#0a6cbc;
  --blue-dark:#08569a;
  --ink:#333;
  --grey-text:#666;
  --topbar:#4a4a4a;
  --band:#3b3b3b;
  --footer:#f1f1f1;
  --bottom:#e6e6e6;
  --white:#fff;
}
*{margin:0;padding:0;box-sizing:border-box}
html,body{width:950px;height:1200px;overflow:hidden;background:var(--white)}
body{position:relative;font-family:"PT Sans",sans-serif;color:var(--ink)}
.abs{position:absolute}
ul{list-style:none}

.topbar{left:0;top:0;width:950px;height:22px;background:var(--topbar)}
.topbar nav{position:absolute;right:150px;top:6px;font-size:6.5px;color:#fff;display:flex;gap:10px;text-transform:uppercase}
.topbar nav span.sep{opacity:.7}

.brand{left:142px;top:48px;font-size:19px;font-weight:700;color:#1b2b44;letter-spacing:-.3px}
.brand b{color:var(--blue)}
.header-links{top:54px;font-size:7.5px;text-transform:uppercase;color:#333}
.contact-label{left:725px;top:43px;font-size:7.5px;text-transform:uppercase}
.contact-phone{left:725px;top:55px;font-size:12.5px;color:var(--blue)}

.mainnav{left:0;top:90px;width:950px;height:28px;background:var(--blue)}
.mainnav ul{position:absolute;left:145px;top:9px;display:flex;gap:13px;font-size:7.5px;font-weight:700;color:#fff;text-transform:uppercase}

.hero{left:0;top:118px;width:950px;height:280px;background:linear-gradient(90deg,#8a7a6e 0%,#c9b8a6 30%,#d9c6b1 50%,#b7a596 75%,#9a8c80 100%)}
.hero-text{left:150px;top:218px;width:270px;color:#2b2b2b}
.hero-text h2{font-size:19px;font-weight:400;color:var(--blue);margin-bottom:8px}
.hero-text p{font-size:10px;line-height:16px}
.hero-btn{left:148px;top:314px;width:161px;height:32px;background:#4a4a4a;color:#fff;font-size:12px;display:flex;align-items:center;justify-content:center;border-radius:2px}
.dropdown{left:142px;top:118px;width:130px;background:var(--blue)}
.dropdown li{height:22.4px;line-height:22.4px;padding-left:15px;font-size:6px;color:#fff;text-transform:uppercase;border-bottom:1px solid #3d8bd0}
.dropdown li:first-child{background:var(--blue-dark)}

.band{left:0;top:398px;width:950px;height:60px;background:var(--band)}
.band p{position:absolute;left:144px;top:15px;width:510px;font-size:8.5px;line-height:16px;color:#ccc;text-transform:uppercase}
.btn-blue{background:linear-gradient(#1b7fd0,var(--blue-dark));color:#fff;display:flex;align-items:center;justify-content:center;border-radius:2px;text-transform:uppercase}
.band .btn-blue{position:absolute;left:669px;top:15px;width:137px;height:29px;font-size:9.5px;font-weight:700}

.welcome{left:0;top:478px;width:950px;text-align:center}
.welcome h1{font-size:19.5px;color:#444;font-weight:700}
.welcome p{width:600px;margin:12px auto 0;font-size:7px;line-height:13.5px;color:var(--grey-text)}

.service{top:577px;width:159px;height:70px;background:var(--blue);color:#fff;text-align:center}
.service h3{position:absolute;bottom:13px;width:100%;font-size:9.5px;font-weight:700;text-transform:uppercase}
.service svg{position:absolute;left:64px;top:10px}
.service-list{top:659px;font-size:6.2px;text-transform:uppercase;color:#555}
.service-list li{height:13.6px;padding-left:13px;position:relative}
.service-list li::before{content:"";position:absolute;left:4px;top:2px;border-left:3px solid #6aa84f;border-top:2.5px solid transparent;border-bottom:2.5px solid transparent}

.login-title{top:814px;font-size:10.5px;font-weight:700;color:var(--blue);text-transform:uppercase}
.login-art{width:70px;height:70px}
.login-text{top:848px;width:215px;font-size:6.5px;line-height:12px;color:#666}
.login-btn{top:902px;width:109px;height:24px;font-size:9.5px}
.divider-v{left:465px;top:838px;width:1px;height:70px;background:#ddd}

.clients-rule{left:0;top:945px;width:950px;height:1px;background:#e3e3e3}
.clients-title{left:0;top:955px;width:950px;text-align:center;font-size:10px;color:#555}
.clients{left:150px;top:983px;width:650px;display:flex;justify-content:space-between;font-size:15px;color:#777}

.footer{left:0;top:1020px;width:950px;height:130px;background:var(--footer)}
.fcol{top:1036px}
.fcol h4{font-size:9px;font-weight:400;color:var(--blue);margin-bottom:5px}
.fcol li{font-size:8.3px;height:16.3px;color:#444}
.fcol li::before{content:"• ";color:#888}
.fcol li.cont{padding-left:36px;height:19px;padding-top:3px}
.fcol li.cont::before{content:none}
.bottom{left:0;top:1150px;width:950px;height:50px;background:var(--bottom)}
.bottom p{position:absolute;left:150px;top:18px;font-size:8.5px;color:#555}
.social{top:1166px;width:15px;height:15px}
</style>
</head>
<body>

<header>
  <div class="abs topbar">
    <nav><span>Home</span><span class="sep">|</span><span>About Us</span><span class="sep">|</span><span>Request a Quote</span><span class="sep">|</span><span>Contact Us</span><span class="sep">|</span><span>Sitemap</span></nav>
  </div>
  <div class="abs brand">Harborline <b>PEO</b></div>
  <span class="abs header-links" style="left:327px">Client Login</span>
  <span class="abs header-links" style="left:414px">Employee Login</span>
  <span class="abs header-links" style="left:514px">Referral Rewards</span>
  <span class="abs header-links" style="left:624px">Demo</span>
  <svg class="abs" style="left:682px;top:40px" width="36" height="34" viewBox="0 0 36 34">
    <rect x="4" y="4" width="28" height="24" rx="4" fill="#333"/>
    <rect x="8" y="7" width="20" height="12" fill="#ccd"/>
    <ellipse cx="18" cy="31" rx="15" ry="2" fill="#ccc"/>
  </svg>
  <span class="abs contact-label">Contact Us</span>
  <span class="abs contact-phone">1.800.555.0142</span>
  <div class="abs mainnav">
    <ul>
      <li>PEO Payroll Services ⌄</li><li>PEO HR Solutions ⌄</li><li>PEO Online Services ⌄</li><li>PEO Workers Compensation ⌄</li><li>PEO Employee Benefits ⌄</li><li>PEO Industry Resources ⌄</li>
    </ul>
  </div>
</header>

<section>
  <div class="abs hero" role="img" aria-label="Photo of smiling employees in a bright office"></div>
  <svg class="abs" style="left:79px;top:252px" width="26" height="26"><circle cx="13" cy="13" r="12" fill="none" stroke="#fff" stroke-opacity=".6" stroke-width="1.5"/><path d="M15 8 10 13 15 18" fill="none" stroke="#fff" stroke-opacity=".7" stroke-width="1.5"/></svg>
  <svg class="abs" style="left:838px;top:252px" width="26" height="26"><circle cx="13" cy="13" r="12" fill="none" stroke="#fff" stroke-opacity=".6" stroke-width="1.5"/><path d="M11 8 16 13 11 18" fill="none" stroke="#fff" stroke-opacity=".7" stroke-width="1.5"/></svg>
  <div class="abs hero-text">
    <h2>WELCOME TO HARBORLINE PEO</h2>
    <p>By turning your back office over to Harborline PEO, you gain a business partner with the expertise you need to ensure your business stays in compliance.</p>
  </div>
  <div class="abs hero-btn">REQUEST A QUOTE</div>
  <ul class="abs dropdown">
    <li>Payroll Administration</li><li>Payroll Tax Filing Services</li><li>Online Payroll Entry</li><li>Paycard</li><li>General Ledger Interface</li><li>ASO Services</li><li>Request a Quote</li><li>Harborline PEO Time</li>
  </ul>
  <div class="abs band">
    <p>By turning your back office over to Harborline PEO, you gain a business partner with the expertise you need to ensure your business stays in compliance. Request a Quote</p>
    <div class="btn-blue">Request a Quote</div>
  </div>
</section>

<section class="abs welcome">
  <h1>WELCOME TO HARBORLINE PEO</h1>
  <p>Advantage Harborline PEO By turning your back office over to Harborline PEO, you gain a business partner with the expertise you need to ensure your business stays in compliance. Request A Quote Helping Your Business Grow Reducing turnover, enhancing employee morale and attracting better employees are integral parts of Harborline PEO's strategy to positively affect your bottom line.</p>
</section>

<section>
  <div class="abs service" style="left:142px">
    <svg width="30" height="30" viewBox="0 0 30 30"><circle cx="15" cy="15" r="13" fill="none" stroke="#fff" stroke-width="2"/><path d="M2 15h26M15 2c-6 7-6 19 0 26M15 2c6 7 6 19 0 26" fill="none" stroke="#fff" stroke-width="1.5"/></svg>
    <h3>Human Resources</h3>
  </div>
  <div class="abs service" style="left:311px">
    <svg width="30" height="30" viewBox="0 0 30 30"><path d="M3 27h25" stroke="#fff" stroke-width="2"/><rect x="5" y="4" width="5" height="22" fill="#fff"/><rect x="12" y="12" width="5" height="14" fill="#fff"/><rect x="19" y="18" width="5" height="8" fill="#fff"/></svg>
    <h3>Payroll Services</h3>
  </div>
  <div class="abs service" style="left:480px">
    <svg width="30" height="30" viewBox="0 0 30 30"><path d="M5 13a10 10 0 0 1 18-4M25 17a10 10 0 0 1-18 4" fill="none" stroke="#fff" stroke-width="3"/><path d="M19 5l6 0 0 6zM11 25l-6 0 0-6z" fill="#fff"/></svg>
    <h3>Worker's Comp</h3>
  </div>
  <div class="abs service" style="left:648px">
    <svg width="30" height="30" viewBox="0 0 30 30"><circle cx="15" cy="8" r="6" fill="#fff"/><path d="M4 28v-8a6 6 0 0 1 6-6h10a6 6 0 0 1 6 6v8z" fill="#fff"/></svg>
    <h3>About HPEO</h3>
  </div>

  <ul class="abs service-list" style="left:145px">
    <li>Training &amp; Development</li><li>Employee Handbooks</li><li>Labor Law Compliance</li><li>Job Descriptions</li><li>Help Center</li><li>Recruiting</li><li>Career Opportunities</li><li>Background Screening</li><li>HPEO Websmart</li><li>WorkCheck</li>
  </ul>
  <ul class="abs service-list" style="left:314px">
    <li>Payroll Administration</li><li>Tax Payment and Filing</li><li>Online Payroll Entry</li><li>Paycard</li><li>Time &amp; Attendance</li><li>General Ledger Interface</li><li>ASO Services</li><li>HPower</li>
  </ul>
  <ul class="abs service-list" style="left:483px">
    <li>Policy Administration</li><li>Injury Claim Administration</li><li>Safety Compliance &amp; Audits</li><li>Safety Compliance Services</li><li>Safety Training Classes</li>
  </ul>
  <ul class="abs service-list" style="left:651px">
    <li>Press Releases</li><li>Articles</li><li>Testimonials</li><li>Case Studies</li><li>Bio's</li><li>What is a PEO?</li><li>Blog</li>
  </ul>
</section>

<section>
  <h2 class="abs login-title" style="left:142px">Client Login</h2>
  <div class="abs login-art" style="left:145px;top:843px;border-radius:50%;background:radial-gradient(circle at 35% 35%,#8fd0f5,#1a78c2)" role="img" aria-label="Illustration of a globe with a cursor"></div>
  <p class="abs login-text" style="left:234px">By turning your back office over to Harborline PEO, you gain a business partner with the expertise you need to ensure your business stays in compliance. Request A Quote Helping Your Business Grow Reducing turnover, enhancing employee...</p>
  <div class="abs btn-blue login-btn" style="left:234px">Client Login</div>
  <div class="abs divider-v"></div>
  <h2 class="abs login-title" style="left:497px">Employee Login</h2>
  <div class="abs login-art" style="left:484px;top:850px;width:84px;height:60px;background:linear-gradient(#e4e4ea,#9a9aa6);border-radius:4px" role="img" aria-label="Illustration of a drawing tablet with a stylus"></div>
  <p class="abs login-text" style="left:588px">By turning your back office over to Harborline PEO, you gain a business partner with the expertise you need to ensure your business stays in compliance. Request A Quote Helping Your Business Grow Reducing turnover, enhancing employee...</p>
  <div class="abs btn-blue login-btn" style="left:589px">Employee Login</div>
</section>

<section>
  <div class="abs clients-rule"></div>
  <p class="abs clients-title">Our Clients</p>
  <div class="abs clients">
    <span>Greenvale</span><span>Lumora</span><span>Netlink</span><span>Sprigg</span><span>Kyrano</span><span>Tellar</span><span>Northsoft</span><span>Ardent</span><span>Cirro</span>
  </div>
</section>

<footer>
  <div class="abs footer"></div>
  <div class="abs fcol" style="left:162px"><h4>Cras mollipurus</h4><ul><li>Integer lobortis</li><li>Curabitur ac</li><li>Phasellus tellus nisl</li><li>Aenean fringilla</li><li>Aliquam commodo</li></ul></div>
  <div class="abs fcol" style="left:296px"><h4>Cras mollipurus</h4><ul><li>Integer lobortis</li><li>Curabitur ac</li><li>Phasellus tellus nisl</li><li>Aenean fringilla</li><li>Aliquam commodo</li></ul></div>
  <div class="abs fcol" style="left:430px"><h4>Cras mollipurus</h4><ul><li>Integer lobortis</li><li>Curabitur ac</li><li>Phasellus tellus nisl</li><li>Aenean fringilla</li><li>Aliquam commodo</li></ul></div>
  <div class="abs fcol" style="left:565px"><h4>Cras mollipurus</h4><ul><li>Integer lobortis</li><li>Curabitur ac</li><li>Phasellus tellus nisl</li><li>Aenean fringilla</li><li>Aliquam commodo</li></ul></div>
  <div class="abs fcol" style="left:695px"><h4>Contact us</h4><ul><li>Phone : 555 310 2241</li><li class="cont">555 3104478</li><li>E-mail : info@harborlinepeo.com</li></ul></div>
  <div class="abs bottom"><p>Copyright © 2013 &nbsp;Harborline PEO, LLC. &nbsp;All Rights Reserved.</p></div>
  <div class="abs social" style="left:766px;background:#3b5a9a" role="img" aria-label="Social profile link"></div>
  <div class="abs social" style="left:786px;background:#5fb6e8" role="img" aria-label="Social profile link"></div>
</footer>

</body>
</html>
```